Tamsin Vale Chiropractic Web Design

We need a fully operating Web site design INCLUDING the code for a Chiropractic Clinic based in Auckland New Zealand to target people from different financial backgrounds.

We need 4 Pages as followed:
1. Home: includes Slideshow of the clinic, General information about chiropractic, option for "Request an appointment", and it would be nice to have a picture on the top right side of the header and the clinic's name and logo on the top left side. on the bottom right we would like a small section for "Testimonial" (A good example: http://www.brindlemoorstudios.example/ )
(A good example for slide show is: http://www.pelvoro.example.nz/)
(A good example for the header is: http://www.spinehavenwelt.example.com/)

2. About Us: this section will include the background information of the company, and a section for our staff (which will includes a photo and description of each person/staff which can be changedanytime)
(a good example: http://www.fernwaybackcare.example.nz/)

3. Contact: includes location, map, contact numbers, email, and a contact box (A good example: http://www.brindlemoorstudios.example/contact/)

4. Services: includes our products, adjustment equipment, chiropractic products for sale, few pictures of patients while under chiropractic care/adjustment tables

We would also like to add "social networking" options on the bottom left side of every page (Facebook, twitter, Blog, Google+)

Please check the following links to get a feel of our favorite designs:
http://www.spinehavenwelt.example.com/
http://www.fernwaybackcare.example.nz/
http://www.pelvoro.example.nz/
http://www.dunmerespinalcentre.example.com/
http://www.quietbirch.example.nz/
http://www.pwo.example.nz/index-1.html
http://home.corelinespine.example.nz/home/

we would like to have full access to the back-end- admin of the website to be able to change and add any pictures or texts.
Updates

Hi Lovely Designer,

thank you so much for your proposed designs. We just uploaded the original source file of our logo, for you all to have access on it to facilitate your work. 

Enjoy your day

Leni

Target Market(s)

People with different financial background as well as we are located in the artistic part of town, so appealing to those crowd is important to us.

Industry/Entity Type

Financial

Requirements
Must have
• 1.color similar to the logo or darker colors (Dark and rich colors are prefered)
2. more artistic than a basic doctors' clinic
3. I would like the opening of the web to bring art, tranquility and peaceful images into mind
Should not have
• Not bombarded with lots of info and pics in one page, not too busy and crowded

```html
<!DOCTYPE html>
<html lang="en">
<head>
<meta charset="utf-8">
<title>Tamsin Vale Chiropractic — Home</title>
<link rel="stylesheet" href="https://fonts.googleapis.com/css2?family=Didact+Gothic&family=Open+Sans:wght@400;600&family=PT+Sans:wght@400;700&display=swap">
<style>
  :root {
    --plum: #6a1158;
    --plum-deep: #5a0c4b;
    --plum-light: #8a2a78;
    --navy: #0f2f5f;
    --navy-deep: #0a2248;
    --nav-text: #1c3566;
    --body-text: #666666;
    --ink: #222222;
    --page-top: #e6ddd5;
    --page-bottom: #ffffff;
    --caption-band: rgba(40, 80, 135, 0.78);
    --social-one: #3b63a8;
    --social-two: #7cc0e8;
    --social-three: #3a3a3a;
    --social-four: #f07a1a;
  }
  * { box-sizing: border-box; margin: 0; padding: 0; }
  html, body { width: 1200px; height: 1200px; overflow: hidden; }
  body {
    position: relative;
    background: linear-gradient(to bottom, var(--page-top) 0px, #efe9e4 300px, var(--page-bottom) 620px);
    font-family: "Open Sans", sans-serif;
    color: var(--body-text);
  }
  h1, h2, h3 { font-weight: 400; }
  .top-rule { position: absolute; left: 0; top: 0; width: 1200px; height: 4px; background: var(--plum-deep); }

  .brand {
    position: absolute; left: 122px; top: 45px; width: 172px; height: 98px;
    background: radial-gradient(circle at 30% 40%, #1d4580 0%, var(--navy) 55%, var(--navy-deep) 100%);
    display: flex; align-items: center; justify-content: center; gap: 8px;
  }
  .brand-mark { width: 8px; height: 8px; border-radius: 50%; background: #c8d9a0; flex: none; }
  .brand-name { font-family: "Didact Gothic", sans-serif; font-size: 13px; line-height: 15px; color: #e8eedd; }

  .main-nav {
    position: absolute; left: 299px; top: 45px; width: 784px; height: 98px;
    background: #ffffff;
    box-shadow: 0 10px 10px -6px rgba(0,0,0,0.35);
    display: flex;
  }
  .main-nav a {
    font-family: "Didact Gothic", sans-serif; font-size: 15px; color: var(--nav-text);
    text-decoration: none; display: flex; align-items: flex-end; justify-content: center;
    padding-bottom: 25px; height: 98px;
  }
  .main-nav a.current { background: var(--plum); color: #ffffff; width: 187px; }
  .main-nav a:nth-child(2) { width: 192px; }
  .main-nav a:nth-child(3) { width: 206px; }
  .main-nav a:nth-child(4) { width: 199px; }

  .hero {
    position: absolute; left: 123px; top: 177px; width: 959px; height: 490px;
    background:
      radial-gradient(ellipse at 50% 55%, #a9c6de 0%, rgba(169,198,222,0) 45%),
      linear-gradient(to bottom, #8fb55a 0%, #6f9a3c 35%, #9bb8c9 70%, #5f7fa6 100%);
  }
  .hero-caption {
    position: absolute; left: 0; bottom: 0; width: 100%; height: 68px;
    background: var(--caption-band);
    display: flex; align-items: center; justify-content: center;
    padding-top: 12px;
    font-family: "Didact Gothic", sans-serif; font-size: 27px; letter-spacing: 0.8px; color: #ffffff;
  }

  .section-title {
    position: absolute; font-family: "Didact Gothic", sans-serif; font-size: 23px; letter-spacing: 1.1px; color: var(--plum);
  }
  .welcome-title { left: 123px; top: 691px; letter-spacing: 0.6px; }
  .reason-title { left: 122px; top: 884px; }
  .copy { position: absolute; left: 121px; width: 580px; font-size: 14.5px; line-height: 23.7px; color: var(--body-text); }
  .welcome-copy { top: 742px; }
  .reason-copy { top: 935px; }
  .reason-copy strong { font-weight: 600; color: var(--ink); }

  .hours {
    position: absolute; left: 775px; top: 698px; width: 305px;
    font-family: "PT Sans", sans-serif; color: var(--ink);
  }
  .hours-title { text-align: center; font-size: 17.5px; margin-left: -55px; }
  .hours-table { margin: 23px 0 0 19px; border-collapse: collapse; font-size: 17px; }
  .hours-table td { padding: 0; line-height: 24px; }
  .hours-table td.day { width: 103px; }
  .hours-table td.sep { width: 12px; }

  .appointment {
    position: absolute; left: 775px; top: 802px; width: 305px; height: 54px;
    background: linear-gradient(to bottom, var(--plum-light) 0%, var(--plum) 55%, var(--plum-deep) 100%);
    border-radius: 6px 6px 3px 3px;
    font-family: "PT Sans", sans-serif; font-size: 21px; color: #ffffff;
    display: flex; align-items: center; justify-content: center; text-decoration: none;
    padding-top: 6px;
    box-shadow: 0 2px 3px rgba(0,0,0,0.2);
  }
  .appointment-reflection {
    position: absolute; left: 775px; top: 856px; width: 305px; height: 28px;
    background: linear-gradient(to bottom, rgba(138,42,120,0.35), rgba(138,42,120,0));
  }

  .testimonials { position: absolute; left: 775px; top: 886px; width: 305px; text-align: center; font-family: "PT Sans", sans-serif; color: var(--ink); }
  .testimonials-title { font-size: 20.5px; color: var(--plum); margin-left: -22px; }
  .testimonials blockquote { margin-top: 24px; font-family: "Open Sans", sans-serif; font-size: 14.5px; line-height: 23.7px; color: var(--ink); }

  .social { position: absolute; left: 122px; top: 1121px; display: flex; gap: 6px; }
  .social span { width: 34px; height: 34px; border-radius: 4px; display: block; }
  .social .social-one { background: var(--social-one); }
  .social .social-two { background: var(--social-two); }
  .social .social-three { background: var(--social-three); }
  .social .social-four { background: var(--social-four); }

  .footer-nav { position: absolute; left: 122px; top: 1180px; font-family: "Didact Gothic", sans-serif; font-size: 13px; color: var(--ink); }
  .footer-nav a { position: absolute; white-space: nowrap; color: var(--ink); text-decoration: none; }
</style>
</head>
<body>
  <div class="top-rule"></div>

  <header>
    <div class="brand"><span class="brand-mark"></span><span class="brand-name">Tamsin Vale<br>Chiropractic</span></div>
    <nav class="main-nav">
      <a class="current" href="#">Home</a>
      <a href="#">About us</a>
      <a href="#">Services</a>
      <a href="#">Contact us</a>
    </nav>
  </header>

  <section class="hero" role="img" aria-label="Slideshow photo of a smiling multi-generation family outdoors among green trees">
    <div class="hero-caption">Chiropractic is the natural family health choice</div>
  </section>

  <h1 class="section-title welcome-title">Welcome to Tamsin Vale Chiropractic</h1>
  <p class="copy welcome-copy">Lorem ipsum dolor sit amet, consectetuer adipiscing elit, sed diam nonummy nibh euismod tincidunt ut laoreet dolore magna aliquam erat volutpat. Ut wisi enim ad minim veniam, quis nostrud exerci tation ullamcorper suscipit lobortis nisl ut aliquip ex ea commodo consequat.</p>

  <h2 class="section-title reason-title">Reason to choose Chiropractic Treatment</h2>
  <p class="copy reason-copy"><strong>Nam liber tempor cum soluta nobis eleifend option congue nihil imperdiet<br>doming id quod mazim placerat facer possim assum.</strong><br>Typi non habent claritatem insitam; est usus legentis in iis qui facit eorum claritatem. Investigationes demonstraverunt lectores legere me lius quod ii legunt saepius. Claritas est etiam processus dynamicus, qui sequitur mutationem consuetudium lectorum.</p>

  <aside class="hours">
    <h3 class="hours-title">PRACTICE HOURS</h3>
    <table class="hours-table">
      <tr><td class="day">Weekdays</td><td class="sep">:</td><td>9.30 a.m - 9 p.m</td></tr>
      <tr><td class="day">Weekends</td><td class="sep">:</td><td>10.30 a.m - 9 p.m</td></tr>
    </table>
  </aside>

  <a class="appointment" href="#">REQUEST AN APPOINTMENT</a>
  <div class="appointment-reflection"></div>

  <aside class="testimonials">
    <h3 class="testimonials-title">TESTIMONIALS</h3>
    <blockquote>“Lorem ipsum dolor sit amet, consectetuer adipiscing elit, sed diam nonummy nibh euismod tincidunt ut laoreet dolore magna aliquam etis nisl ut aliquip ex ea commodo consequat. ”</blockquote>
  </aside>

  <footer>
    <div class="social" aria-label="Social links">
      <span class="social-one"></span>
      <span class="social-two"></span>
      <span class="social-three"></span>
      <span class="social-four"></span>
    </div>
    <nav class="footer-nav">
      <a href="#" style="left:0">Home</a>
      <a href="#" style="left:107px">About us</a>
      <a href="#" style="left:229px">Services</a>
      <a href="#" style="left:347px">Contact us</a>
    </nav>
  </footer>
</body>
</html>
```